Cardivo Comparison Site requires banner adds

At Quotevale.com.au we are a free service that allows our customers to get up to five quotes from our panel of suppliers for a range of BUSINESS related products and services. These products include cardivo / credit card machines, bank accounts, insurance, signage,office furniture etc. basically anything that a small business would need.
The process is done in 3 steps; 1) register your enquiry 2) we source and provide the five cheapest quotes 3) then select the supplier of your choice,the process is simple 123 and is FREE.

Please visit the soon to be revamped website to see our current horrible banner adds.
I require 8 banner adds with the below information
ADD 1) Get up to 10 quotes here FREE
Add 2) Australia's only CARDIVO comparison site
Add 3) Ringing everywhere for quotes.............it's so yesterday!
Add 4) Hate Cardivo Fee? Cardivo surcharging now available.
Add 5) Cardivo eating your profits? Let us put your Cardivo on a diet
Add 6) Pay less for "Lumo logo" "Brightpass Logo" "Cardivo Logo"
Add 7) Get "Flick Swift" now
Add 8) We guarantee to get you a better deal than your bank!

Reason: I am extending your deadline because there are 8 banners and i dont want to rush you given that you have so many designs to work on.

Target Market(s)

small and medium business operators

Industry/Entity Type

Small Business

Requirements
Must have
• must have images and be bold

```html
<!DOCTYPE html>
<html lang="en">
<head>
<meta charset="utf-8">
<title>Hate Cardivo Fee? Cardivo Surcharging Now Available</title>
<link rel="stylesheet" href="https://fonts.googleapis.com/css2?family=Roboto+Condensed:wght@300;700&display=swap">
<style>
  :root {
    --ink: #111111;
    --accent-red: #e0000f;
    --glow: #ffffff;
    --mid-grey: #cfcfcf;
    --edge-grey: #7d7d7d;
    --tick-light: #c9c9c9;
    --tick-dark: #9a9a9a;
  }
  html, body {
    margin: 0;
    padding: 0;
    width: 1200px;
    height: 299px;
    overflow: hidden;
  }
  .banner {
    position: relative;
    width: 1200px;
    height: 299px;
    overflow: hidden;
    background:
      radial-gradient(ellipse 62% 78% at 50% 48%, var(--glow) 0%, #f4f4f4 40%, var(--mid-grey) 75%, var(--edge-grey) 100%);
  }
  .headline {
    position: absolute;
    left: 233px;
    top: 44px;
    margin: 0;
    font-family: "Roboto Condensed", "Arial Narrow", sans-serif;
    text-transform: uppercase;
    color: var(--ink);
    line-height: 1;
  }
  .headline span { display: block; }
  .headline__question {
    font-weight: 300;
    font-size: 66px;
    letter-spacing: 1px;
  }
  .headline__offer {
    font-weight: 700;
    font-size: 50px;
    letter-spacing: 1.5px;
    margin-top: 6px;
  }
  .headline__status {
    font-weight: 700;
    font-size: 90px;
    letter-spacing: 2px;
    color: var(--accent-red);
    margin-top: 0;
  }
  .tick-icon {
    position: absolute;
    left: 960px;
    top: 80px;
    width: 124px;
    height: 124px;
  }
</style>
</head>
<body>
  <main class="banner">
    <h1 class="headline">
      <span class="headline__question">Hate Cardivo Fee?</span>
      <span class="headline__offer">Cardivo Surcharging</span>
      <span class="headline__status">Now Available</span>
    </h1>
    <svg class="tick-icon" viewBox="0 0 124 124" aria-hidden="true">
      <defs>
        <linearGradient id="tick-fill" x1="0" y1="0" x2="1" y2="1">
          <stop offset="0" stop-color="var(--tick-light)"/>
          <stop offset="1" stop-color="var(--tick-dark)"/>
        </linearGradient>
      </defs>
      <path d="M4 70 C14 62 24 60 32 66 C38 72 42 84 44 92 C62 52 88 22 120 2 C96 30 70 70 54 118 C50 122 40 122 36 118 C30 100 20 84 4 70 Z"
            fill="url(#tick-fill)" opacity="0.85"/>
    </svg>
  </main>
</body>
</html>
```